Dietitian needs a new business card design

I need a new business card design for my nutrition business that provides individual clinical nutrition advice for people with medical conditions. Business cards will be handed out to doctors, specialists and clients so will need to be sharp and project an image of professionalism

Target Market(s)

My clients are typically referred by doctors or specialists and the card will be used to handout to clients and their doctors.

Industry/Entity Type

Medical

Contact Information for Business Card

The business card will require the details below. These details can be found from my website https://www.kelvarrowclinic.com.au/

Font styles to use
Serif

Colors

Designer to choose colors to be used in the design.

Requirements
Must have
• 1. It needs be professional and contemporary
• 2. It needs to incorporate my logo
• 3. It needs space to write appointment times and dates
• 4. It needs to provide my phone number, fax number, email address and my web address
Nice to have
• Include the Registered Tovance Clinician Logo
• I have access to Framellow if required
• The locations I practise from
Should not have
• Pictures of food
• Spelling MIstakes

```html
<!DOCTYPE html>
<html lang="en">
<head>
<meta charset="utf-8">
<title>Kelvarrow Nutrition &amp; Dietetics – Business Card</title>
<link rel="stylesheet" href="https://fonts.googleapis.com/css2?family=Tinos:wght@400;700&display=swap">
<style>
  :root {
    --page: #eceae6;
    --card: #ffffff;
    --brand-blue: #0b63b0;
    --badge-orange: #f07d22;
    --rule: #b9b9b9;
    --ink: #1f1f1f;
    --ghost: rgba(11, 99, 176, 0.09);
  }
  * { box-sizing: border-box; margin: 0; padding: 0; }
  html, body { width: 1200px; height: 1200px; overflow: hidden; }
  body {
    background: var(--page);
    font-family: "Tinos", "Times New Roman", serif;
    position: relative;
  }
  .card {
    position: absolute;
    left: 190px;
    width: 820px;
    height: 500px;
    background: var(--card);
    box-shadow: 0 6px 18px rgba(0,0,0,0.18);
    overflow: hidden;
  }
  .card--front { top: 60px; }
  .card--back { top: 620px; }

  /* Front */
  .brand { position: absolute; left: 48px; top: 58px; display: flex; align-items: center; gap: 22px; }
  .brand__dot { width: 120px; height: 120px; border-radius: 50%; background: var(--brand-blue); flex: none; }
  .brand__name { color: var(--brand-blue); font-weight: 400; font-size: 50px; line-height: 1.08; }
  .person-name {
    position: absolute; left: 385px; top: 215px;
    color: var(--brand-blue); font-weight: 700; font-size: 38px;
  }
  .contact {
    position: absolute; left: 58px; top: 340px;
    color: var(--brand-blue); font-size: 27px; line-height: 1.28; list-style: none;
  }
  .accreditation {
    position: absolute; right: 30px; top: 380px;
    width: 198px; height: 100px; border-radius: 6px; background: var(--badge-orange);
  }

  /* Back */
  .ghost-brand {
    position: absolute; left: 40px; top: 120px;
    display: flex; align-items: center; gap: 30px;
  }
  .ghost-brand__dot { width: 230px; height: 230px; border-radius: 50%; background: var(--ghost); flex: none; }
  .ghost-brand__name { color: var(--ghost); font-size: 96px; line-height: 1; }
  .appointment__title {
    position: absolute; left: 55px; top: 24px;
    color: var(--brand-blue); font-weight: 700; font-size: 42px; letter-spacing: 1px;
  }
  .slots {
    position: absolute; width: 320px;
    display: flex; flex-direction: column; gap: 24px;
  }
  .slots--date { left: 55px; top: 90px; }
  .slots--time { left: 440px; top: 126px; }
  .slot {
    height: 44px;
    font-size: 22px; line-height: 1; color: var(--ink);
    border-bottom: 1px solid var(--rule);
  }
  .note-band {
    position: absolute; left: 0; right: 0; bottom: 0; height: 100px;
    background: var(--brand-blue); color: #fff;
    font-weight: 700; font-size: 28px; padding: 22px 48px;
  }
</style>
</head>
<body>
  <section class="card card--front" aria-label="Business card front">
    <div class="brand">
      <span class="brand__dot" aria-hidden="true"></span>
      <span class="brand__name">Kelvarrow<br>Nutrition &amp; Dietetics</span>
    </div>
    <h1 class="person-name">Martin Ellacott</h1>
    <ul class="contact">
      <li>Tel: 0400 555 182</li>
      <li>Fax: +613 5550 4417</li>
      <li>E-mail: martin@kelvarrowclinic.com.au</li>
      <li>brindlewoodmedical.com.au</li>
    </ul>
    <div class="accreditation" role="img" aria-label="Registered Tovance Clinician badge"></div>
  </section>

  <section class="card card--back" aria-label="Business card back">
    <div class="ghost-brand" aria-hidden="true">
      <span class="ghost-brand__dot"></span>
      <span class="ghost-brand__name">Kelvarrow</span>
    </div>
    <h2 class="appointment__title">APPOINTMENT</h2>
    <div class="slots slots--date">
      <div class="slot">Date</div>
      <div class="slot">Date</div>
      <div class="slot">Date</div>
      <div class="slot">Date</div>
    </div>
    <div class="slots slots--time">
      <div class="slot">Time</div>
      <div class="slot">Time</div>
      <div class="slot">Time</div>
      <div class="slot">Time</div>
    </div>
    <div class="note-band">Note</div>
  </section>
</body>
</html>
```